Business Card Design Project

A double sided business card for presentation to business leaders in corporate.

Target Market(s)

Corporate, business professionals, HR

Industry/Entity Type

Business

Requirements
Must have
• FRONT

Logo

www.brightfernco.com.au

BACK

Maren Tollvey-Hart
Director

+ 61 (0) 418 556 230
maren@brightfernco.com.au
www.brightfernco.com.au

Thrive through energy and employee engagement

("ripples" of logo, bottom corner)

Must be:
- double sided
size: 86 x 54mm
supplied as one pdf with crop marks shown (+- 1mm, with 2-3 mm bleed)

```html
<!DOCTYPE html>
<html lang="en">
<head>
<meta charset="utf-8">
<title>Bright Fern Co – Business Card</title>
<link rel="stylesheet" href="https://fonts.googleapis.com/css2?family=Mulish:wght@400;600;700&family=Arimo:ital,wght@0,400;0,600;0,700;1,400&family=Patrick+Hand&display=swap">
<style>
  :root {
    --page: #ffffff;
    --frame: #222222;
    --slate: #3c4546;
    --violet: #6a0d91;
    --ink-light: #ffffff;
  }
  html, body {
    margin: 0;
    padding: 0;
    overflow: hidden;
    background: var(--page);
  }
  .sheet {
    position: relative;
    width: 1200px;
    height: 902px;
    box-sizing: border-box;
    border: 2px solid var(--frame);
    background: var(--page);
    overflow: hidden;
  }
  .card {
    position: absolute;
    top: 203px;
    width: 322px;
    height: 512px;
    color: var(--ink-light);
  }
  .card--front {
    left: 259px;
    background: var(--slate);
    border-top-left-radius: 50px;
  }
  .card--back {
    left: 631px;
    background: var(--violet);
    border-top-right-radius: 50px;
  }
  .brand {
    position: absolute;
    display: flex;
    align-items: center;
    font-family: "Mulish", sans-serif;
    font-weight: 400;
    color: var(--ink-light);
    white-space: nowrap;
  }
  .brand__dot {
    border: 2px solid var(--ink-light);
    border-radius: 50%;
    box-sizing: border-box;
  }
  .card--front .brand {
    left: 66px;
    top: 236px;
    font-size: 25px;
    gap: 9px;
  }
  .card--front .brand__dot {
    width: 38px;
    height: 38px;
  }
  .card--back .brand {
    left: 45px;
    top: 50px;
    font-size: 18px;
    gap: 7px;
  }
  .card--back .brand__dot {
    width: 26px;
    height: 26px;
  }
  .front-url {
    position: absolute;
    left: 0;
    right: 0;
    top: 460px;
    text-align: center;
    font-family: "Mulish", sans-serif;
    font-weight: 600;
    font-size: 19px;
    letter-spacing: 0.4px;
  }
  .tagline {
    position: absolute;
    left: 45px;
    top: 127px;
    margin: 0;
    font-family: "Patrick Hand", cursive;
    font-size: 18px;
    line-height: 28px;
    letter-spacing: 1.2px;
  }
  .person {
    position: absolute;
    left: 45px;
    top: 338px;
    margin: 0;
  }
  .person__name {
    display: block;
    font-family: "Arimo", sans-serif;
    font-weight: 600;
    font-size: 17.5px;
    letter-spacing: 1.6px;
  }
  .person__role {
    display: block;
    font-family: "Arimo", sans-serif;
    font-style: italic;
    font-size: 12px;
    letter-spacing: 2px;
    margin-top: 2px;
  }
  .contact {
    position: absolute;
    left: 45px;
    top: 406px;
    margin: 0;
    padding: 0;
    list-style: none;
    font-family: "Arimo", sans-serif;
    font-weight: 600;
  }
  .contact li {
    font-size: 14.5px;
    line-height: 26px;
  }
  .contact .contact__phone {
    font-size: 15.5px;
  }
</style>
</head>
<body>
  <main class="sheet">
    <section class="card card--front" aria-label="Card front">
      <div class="brand">
        <span class="brand__dot" aria-hidden="true"></span>
        <span class="brand__name">brightfern co</span>
      </div>
      <div class="front-url">www.brightfernco.com.au</div>
    </section>

    <section class="card card--back" aria-label="Card back">
      <div class="brand">
        <span class="brand__dot" aria-hidden="true"></span>
        <span class="brand__name">brightfern co</span>
      </div>
      <p class="tagline">Thrive through energy and<br>employee engagement</p>
      <p class="person">
        <span class="person__name">Maren Tollvey-Hart</span>
        <span class="person__role">director</span>
      </p>
      <ul class="contact">
        <li class="contact__phone">+ 61 (0) 418 556 230</li>
        <li class="contact__email">maren@brightfernco.com.au</li>
        <li class="contact__web">www.brightfernco.com.au</li>
      </ul>
    </section>
  </main>
</body>
</html>
```